Criminal Defense Law Firm needs Stationary design Theme for a Business Card, Envelope, and Letterhea

Our Law Firm is seeking a general design concept for a business card, letterhead, and Envelope.

Our website is WillowcrestTrialDesk.com

A design for these three items is requested to keep branding in place for the firm. Would like to keep the Firm Colors on the website consistent with our branding on business cards, letterheads, and mailing envelopes #10 size to be exact.

We would like business cards printed front and back with Law firm Colors from website.

Letterhead with law firm colors as well. Design is not limited to just the header, but the footer can be utilized as well for email, website, phone, fax, etc.

Simple #10 envelope consisting of the same design principles set out in the previous two designs.

```html
<!DOCTYPE html>
<html lang="en">
<head>
<meta charset="utf-8">
<title>Willowcrest Trial Offices – Stationery</title>
<link href="https://fonts.googleapis.com/css2?family=Libre+Baskerville:wght@700&family=Open+Sans:wght@400&family=Montserrat:wght@500;600&display=swap" rel="stylesheet">
<style>
:root{
  --teal:#40e6cc;
  --olive:#a09244;
  --ink:#2b2b2b;
  --graphite:#3a3a3a;
  --paper:#ffffff;
  --faint:#e6e6e6;
  --rule:#555;
  --backdrop:#ebe8e4;
}
*{box-sizing:border-box;margin:0;padding:0}
html,body{width:1200px;height:553px;overflow:hidden;background:var(--backdrop)}
.canvas{position:relative;width:1200px;height:553px;font-family:"Open Sans",sans-serif;color:var(--ink)}
.sheet{position:absolute;background:var(--paper);box-shadow:0 2px 6px rgba(0,0,0,.18);overflow:hidden}
.letterhead{left:26px;top:29px;width:347px;height:451px}
.fax-sheet{left:391px;top:29px;width:349px;height:451px}
.brand{position:absolute;display:flex;align-items:center;gap:4px}
.brand-dot{width:15px;height:15px;border:1.3px solid var(--ink);border-radius:50%;flex:none}
.brand-name{font-family:"Libre Baskerville",serif;font-weight:700;font-size:6.6px;line-height:1.15;text-transform:uppercase;color:var(--ink)}
.sheet .brand{left:8px;top:11px}
.contacts{position:absolute;right:13px;top:13px;display:flex;gap:5px;font-family:"Montserrat",sans-serif;font-size:5px;line-height:1.9;text-transform:uppercase;color:var(--ink)}
.contacts .col-web{text-align:right}
.contacts .col-phone{border-left:.8px solid var(--ink);padding-left:5px}
.watermark{position:absolute;left:52px;top:129px;width:224px;height:224px;border:5px solid var(--faint);border-radius:50%}
.address{position:absolute;font-family:"Montserrat",sans-serif;font-weight:500;font-variant:small-caps;text-transform:capitalize;color:var(--ink);white-space:nowrap}
.sheet .address{left:0;right:0;text-align:center;top:430px;font-size:7.5px}
.band{position:absolute;left:0;bottom:0;width:100%}
.fax-title{position:absolute;left:19px;top:82px;font-size:21px;font-weight:400}
.fax-field{position:absolute;height:10px;border-bottom:.8px solid var(--rule);font-size:5.5px;line-height:9px}
.fax-field.left{left:19px;width:167px}
.fax-field.right{left:196px;width:120px}
.fax-checks{position:absolute;left:19px;top:205px;display:flex;gap:12px;font-size:5.5px;align-items:center}
.fax-checks span{display:flex;align-items:center;gap:4px}
.fax-checks i{width:7px;height:7px;border:.8px solid var(--ink);display:inline-block}
.envelope-back{left:788px;top:26px;width:389px;height:173px}
.flap{position:absolute;left:0;top:0}
.envelope-flap{left:776px;top:102px;width:389px;height:98px}
.envelope-front{left:750px;top:189px;width:390px;height:175px}
.envelope-front .brand{left:10px;top:9px}
.envelope-front .address{left:10px;top:36px;font-size:7px;line-height:1.3}
.envelope-front .web{position:absolute;left:10px;top:153px;font-family:"Montserrat",sans-serif;font-weight:600;font-size:6px;text-transform:uppercase}
.card{width:144px;height:82px;top:391px}
.card-front{left:766px}
.card-front .brand{left:22px;top:11px}
.card-front .brand-dot{width:12px;height:12px}
.card-front .brand-name{font-size:5.5px}
.person{position:absolute;left:0;right:0;top:33px;text-align:center;font-family:"Montserrat",sans-serif;font-size:4.6px;line-height:1.35;text-transform:uppercase;font-weight:600}
.person small{display:block;font-weight:500;font-size:4px;font-variant:small-caps;text-transform:none}
.card-lines{position:absolute;left:0;right:0;top:49px;text-align:center;font-family:"Montserrat",sans-serif;font-size:3.6px;line-height:1.7;text-transform:uppercase}
.card-front .address{left:0;right:0;text-align:center;top:69px;font-size:3.8px}
.card-back{left:946px;width:143px}
.card-back .ring{position:absolute;left:43px;top:7px;width:60px;height:60px;border:2px solid var(--faint);border-radius:50%}
.card-back .brand-name{position:absolute;left:12px;top:28px;font-size:9px;line-height:1.2}
.option-label{position:absolute;top:490px;font-size:25px;color:var(--graphite)}
.option-one{left:128px}
.option-two{left:501px}
</style>
</head>
<body>
<main class="canvas">

  <!-- Letterhead, dark footer -->
  <section class="sheet letterhead">
    <div class="brand"><span class="brand-dot"></span><span class="brand-name">Willowcrest Trial<br>Offices</span></div>
    <div class="contacts">
      <div class="col-web">✉ willowcresttrialdesk@mail.com<br>◉ www.willowcresttrialdesk.com</div>
      <div class="col-phone">✆ 555.210.4471<br>✆ 555.318.6620</div>
    </div>
    <div class="watermark"></div>
    <p class="address">2140 Larkspur Avenue, Fairhaven, NM 87000</p>
    <svg class="band" width="347" height="8" viewBox="0 0 347 8" preserveAspectRatio="none">
      <polygon points="0,0 195,0 183,8 0,8" fill="#5a5a5a"/>
      <polygon points="199,0 347,0 347,8 187,8" fill="#0d0d0d"/>
    </svg>
  </section>

  <!-- Fax sheet, brand colour footer -->
  <section class="sheet fax-sheet">
    <div class="brand"><span class="brand-dot"></span><span class="brand-name">Willowcrest Trial<br>Offices</span></div>
    <div class="contacts">
      <div class="col-web">✉ willowcresttrialdesk@mail.com<br>◉ www.willowcresttrialdesk.com</div>
      <div class="col-phone">✆ 555.210.4471<br>✆ 555.318.6620</div>
    </div>
    <h1 class="fax-title">FAX</h1>
    <div class="fax-field left" style="top:119px">To :</div>
    <div class="fax-field right" style="top:119px">From :</div>
    <div class="fax-field left" style="top:137px">Fax :</div>
    <div class="fax-field right" style="top:137px">Pages :</div>
    <div class="fax-field left" style="top:156px">Phone :</div>
    <div class="fax-field right" style="top:156px">Date :</div>
    <div class="fax-field left" style="top:174px">Re :</div>
    <div class="fax-field right" style="top:174px">CC :</div>
    <div class="fax-checks">
      <span><i></i>Urgent</span>
      <span><i></i>For Review</span>
      <span><i></i>Please Comment</span>
      <span><i></i>Please Reply</span>
      <span><i></i>Please Recycle</span>
    </div>
    <p class="address">2140 Larkspur Avenue, Fairhaven, NM 87000</p>
    <svg class="band" width="349" height="8" viewBox="0 0 349 8" preserveAspectRatio="none">
      <polygon points="0,0 160,0 148,8 0,8" fill="var(--teal)"/>
      <polygon points="164,0 349,0 349,8 152,8" fill="var(--olive)"/>
    </svg>
  </section>

  <!-- Envelope back, black flap -->
  <section class="sheet envelope-back">
    <svg class="flap" width="389" height="70" viewBox="0 0 389 70">
      <path d="M0,0 H389 V4 Q380,18 360,22 L218,62 Q194,70 170,62 L29,22 Q9,18 0,4 Z" fill="#0d0d0d"/>
      <circle cx="194" cy="34" r="14" fill="none" stroke="#2a2a2a" stroke-width="1.5"/>
    </svg>
  </section>

  <!-- Envelope back, teal flap -->
  <section class="sheet envelope-flap">
    <svg class="flap" width="389" height="70" viewBox="0 0 389 70">
      <path d="M0,0 H389 V4 Q380,18 360,22 L218,62 Q194,70 170,62 L29,22 Q9,18 0,4 Z" fill="var(--teal)"/>
      <circle cx="194" cy="34" r="14" fill="none" stroke="#1f6f63" stroke-width="1.5"/>
    </svg>
  </section>

  <!-- Envelope front -->
  <section class="sheet envelope-front">
    <div class="brand"><span class="brand-dot"></span><span class="brand-name">Willowcrest Trial<br>Offices</span></div>
    <p class="address">2140 Larkspur Avenue, Fairhaven<br>NM 87000</p>
    <p class="web">◉ www.willowcresttrialdesk.com</p>
    <svg class="band" width="390" height="8" viewBox="0 0 390 8" preserveAspectRatio="none">
      <polygon points="0,0 165,0 153,8 0,8" fill="var(--teal)"/>
      <polygon points="169,0 390,0 390,8 157,8" fill="var(--olive)"/>
    </svg>
  </section>

  <!-- Business card front -->
  <section class="sheet card card-front">
    <div class="brand"><span class="brand-dot"></span><span class="brand-name">Willowcrest Trial<br>Offices</span></div>
    <p class="person">Marcus Ellery<small>Designation</small></p>
    <p class="card-lines">✆ 555.210.4471 &nbsp;✆ 555.318.6620<br>✉ willowcresttrialdesk@mail.com<br>◉ www.willowcresttrialdesk.com</p>
    <p class="address">2140 Larkspur Avenue, Fairhaven, NM 87000</p>
    <svg class="band" width="144" height="4" viewBox="0 0 144 4" preserveAspectRatio="none">
      <polygon points="0,0 70,0 64,4 0,4" fill="var(--teal)"/>
      <polygon points="72,0 144,0 144,4 66,4" fill="var(--olive)"/>
    </svg>
  </section>

  <!-- Business card back -->
  <section class="sheet card card-back">
    <div class="ring"></div>
    <p class="brand-name">Willowcrest Trial<br>Offices</p>
  </section>

  <p class="option-label option-one">Option-1</p>
  <p class="option-label option-two">Option-2</p>
</main>
</body>
</html>
```